The Lantern Guide

I am a life coach specializing in helping people with depression and bipolar disorder. I would like a nice, fun design for a business card.

```html
<!DOCTYPE html>
<html lang="en">
<head>
<meta charset="utf-8">
<title>The Lantern Guide – Business Card</title>
<link href="https://fonts.googleapis.com/css2?family=Oswald:wght@500&family=Arimo:wght@400&display=swap" rel="stylesheet">
<style>
  :root {
    --page-bg: #e9ecec;
    --teal-dark: #04707a;
    --teal-bright: #1fb392;
    --card-light: #f6f7f7;
    --text-light: #ffffff;
    --shadow: rgba(0, 0, 0, 0.18);
  }
  * { margin: 0; padding: 0; box-sizing: border-box; }
  html, body {
    width: 1200px;
    height: 900px;
    overflow: hidden;
    background: var(--page-bg);
  }
  .card {
    position: absolute;
    left: 150px;
    top: 171px;
    width: 900px;
    height: 558px;
    display: flex;
    background: var(--card-light);
    box-shadow: 0 14px 40px var(--shadow);
  }
  .contact-panel {
    position: relative;
    width: 399px;
    height: 100%;
    background: var(--teal-dark);
    color: var(--text-light);
    font-family: "Arimo", Arial, sans-serif;
    text-align: right;
  }
  .accent-stripe {
    width: 12px;
    height: 100%;
    background: var(--teal-bright);
  }
  .holder-name {
    position: absolute;
    right: 30px;
    top: 80px;
    font-family: "Oswald", "Arial Narrow", sans-serif;
    font-weight: 500;
    font-size: 34px;
    line-height: 1;
    white-space: nowrap;
    text-transform: uppercase;
  }
  .holder-title {
    position: absolute;
    right: 34px;
    top: 122px;
    font-size: 23px;
    line-height: 1;
    white-space: nowrap;
  }
  .name-pointer {
    position: absolute;
    right: -58px;
    top: 100px;
    width: 60px;
    height: 14px;
  }
  .contact-list {
    position: absolute;
    right: 30px;
    top: 256px;
    list-style: none;
    font-size: 23px;
    line-height: 33px;
    white-space: nowrap;
  }
  .contact-list li {
    display: flex;
    justify-content: flex-end;
    align-items: center;
    gap: 6px;
  }
  .contact-list svg {
    width: 20px;
    height: 20px;
    fill: var(--text-light);
    flex: none;
  }
  .address {
    position: absolute;
    right: 30px;
    top: 410px;
    font-size: 23px;
    line-height: 32px;
    font-style: normal;
    white-space: nowrap;
  }
  .brand-panel {
    flex: 1;
    display: flex;
    flex-direction: column;
    align-items: center;
    justify-content: center;
    gap: 22px;
  }
  .brand-dot {
    width: 96px;
    height: 96px;
    border-radius: 50%;
    background: var(--teal-bright);
  }
  .brand-name {
    font-family: "Oswald", "Arial Narrow", sans-serif;
    font-weight: 500;
    font-size: 60px;
    line-height: 1.05;
    color: var(--teal-dark);
    text-transform: uppercase;
    text-align: center;
  }
</style>
</head>
<body>
  <section class="card">
    <div class="contact-panel">
      <h1 class="holder-name">Daniel Hartley</h1>
      <p class="holder-title">Managing Director</p>
      <svg class="name-pointer" viewBox="0 0 60 14" aria-hidden="true">
        <polygon points="0,9 60,2 44,14" fill="var(--teal-bright)"/>
      </svg>

      <ul class="contact-list">
        <li>044-555 210 347
          <svg viewBox="0 0 20 20" aria-hidden="true"><path d="M2 7c0-3 4-4 8-4s8 1 8 4v1h-4V6H6v2H2zM5 9h10l2 8H3z"/><circle cx="10" cy="13" r="2" fill="var(--teal-dark)"/></svg>
        </li>
        <li>044-555 210 348
          <svg viewBox="0 0 20 20" aria-hidden="true"><path d="M6 1h8a1 1 0 0 1 1 1v16a1 1 0 0 1-1 1H6a1 1 0 0 1-1-1V2a1 1 0 0 1 1-1zm1 3v11h6V4z"/></svg>
        </li>
        <li>hello@lantern.com
          <svg viewBox="0 0 20 20" aria-hidden="true"><path d="M2 4h16v12H2z"/><path d="M2 4l8 7 8-7" fill="none" stroke="var(--teal-dark)" stroke-width="1.6"/></svg>
        </li>
        <li>www.lanternguide.com
          <svg viewBox="0 0 20 20" aria-hidden="true"><circle cx="10" cy="10" r="8"/><path d="M6 5c2 1 3 3 1 5s1 4 3 5M12 4c0 2 2 3 4 3" fill="none" stroke="var(--teal-dark)" stroke-width="1.6"/></svg>
        </li>
      </ul>

      <address class="address">
        48, Harbor Light Lane<br>
        Fairview Bay, 204518
      </address>
    </div>
    <div class="accent-stripe"></div>
    <div class="brand-panel">
      <div class="brand-dot"></div>
      <p class="brand-name">The Lantern<br>Guide</p>
    </div>
  </section>
</body>
</html>
```